House-share and Room Rental Website (With Focus on the Bedroom Landing Page)

Looking for website design for our House-share (executive accommodation) and room rental business.

Our company name is: Lodvenra could also be written as LodVenra or lodvenra. Either is fine .. just looking for a nice clean catchy logo to go with the design.

EXAMPLES
These are examples of other websites in this field that are doing well. this is a kind of baseline.
https://kelbrin.com.au/
https://www.tuvaplex.com/
https://www.nestorvi.com/
https://www.quillsa.net/
https://www.pendlebarrow.com.au/

Our business model is to rent rooms to people looking for high-quality accommodation. We fill the gap between those looking to rent rooms and those with rooms to rent. However, our model is slightly different from those already on the market as we looking to fill a massive gap in the market delivering upmarket rooms for rent.(Executive Accommodation) also in the back end will be coupled with a self management process in the back end.

We offer executive style accommodation that stands out above the rest. With special extras like fire safety.. and management processes that create happier homes. We are looking for a web design package that can help us grow and scale our business. We need a design that is captivating

Our MAIN focus is having a room landing page that stands out from the rest... The core of our business will rely on the promotion of the rooms in a share house... so the whole design relies on the BEDROOM landing page to drive results.

Target Market(s)

We have 2 markets we are aiming at ... the first market is people offering rooms to rent who want the highest rental return. The second market is people looking to rent safe, high-quality rooms, in houses that are well managed and looked after.

Industry/Entity Type

Share Economy

Logo Text

LodVenra

Number of Pages Required

5+ page

Font styles to use
Sans Serif

Colors
3276b5

Requirements
Must have
• A messaging system whereby we can create direct communication between those offering rooms and those looking for rooms.
• A call to action that says " Schedule an Inspection"
• Landing page for promoting rooms
• A home page for showing stock.
• Profile page for those selling rooms
• Profile page for those looking for rooms.
• A scheduling calendar for booking inspections
Nice to have
• Pages where new residents can lock in a room.. pay bond and rents.. and sign contracts
• Notifications
• SMS capabilities in the backend.
Should not have
• No script or handwriting fonts.

```html
<!DOCTYPE html>
<html lang="en">
<head>
<meta charset="utf-8">
<title>Lodvenra – Room Listing</title>
<link href="https://fonts.googleapis.com/css2?family=Outfit:wght@300;400;500;600&display=swap" rel="stylesheet">
<style>
:root{
  --brand:#3276b5;
  --ink:#1f1f1f;
  --muted:#6b6b6b;
  --orange:#f28c1c;
  --band:#f4f6f9;
  --dark:#2a2728;
  --dark-line:#45403f;
  --field:#5c595a;
  --icon:#555;
  --white:#fff;
}
*{box-sizing:border-box;margin:0;padding:0}
html,body{width:679px;height:1200px;overflow:hidden;background:var(--white)}
body{position:relative;font-family:"Outfit",sans-serif;color:var(--ink)}
.abs{position:absolute}

/* header */
.header{left:0;top:0;width:679px;height:45px;background:var(--white)}
.brand{left:50px;top:9px;display:flex;align-items:center;gap:5px}
.brand-mark{width:11px;height:11px;background:var(--brand)}
.brand-name{font-size:16px;font-weight:500;color:var(--brand)}
.brand-tag{left:50px;top:29px;font-size:6.5px;color:#8a8a8a;letter-spacing:.2px}
.btn-icon{left:408px;top:14px;width:18px;height:17px;border:1px solid var(--brand);border-radius:2px;display:flex;align-items:center;justify-content:center}
.btn-login{left:434px;top:14px;width:82px;height:17px;background:var(--brand);color:var(--white);font-size:7.5px;display:flex;align-items:center;justify-content:center;gap:4px;border-radius:2px}
.btn-inspect{left:525px;top:14px;width:104px;height:17px;border:1px solid var(--brand);color:var(--brand);font-size:7.5px;display:flex;align-items:center;justify-content:center;gap:4px;border-radius:2px}

/* gallery */
.photo{top:45px;height:204px}
.photo-a{left:0;width:113px;background:linear-gradient(160deg,#e9ebea,#b9b4ad 60%,#6d5a48)}
.photo-b{left:116px;width:447px;background:linear-gradient(135deg,#c9b596,#efe7da 45%,#d2a35c 70%,#5a3d2c)}
.photo-c{left:566px;width:113px;background:linear-gradient(180deg,#c9c6bf,#9c978d)}
.gal-arrow{top:137px;width:16px;height:16px;border-radius:50%;background:var(--white);box-shadow:0 1px 3px rgba(0,0,0,.25);display:flex;align-items:center;justify-content:center}

/* listing */
.addr{left:50px;top:293px;font-size:8px;color:var(--muted);display:flex;align-items:center;gap:5px}
.map-link{left:405px;top:293px;font-size:7px;color:var(--brand);text-decoration:underline}
.title{left:50px;top:315px;width:340px;font-size:14px;font-weight:500;line-height:17px}
.meta{left:50px;top:359px;font-size:8px;color:var(--muted)}
.price{left:50px;top:381px;font-size:8.5px;font-weight:600;color:var(--brand)}
.price span{color:var(--orange)}

.house{left:0;top:407px;width:480px;height:106px;background:var(--band)}
.h2{font-size:10.5px;font-weight:500}
.amen{position:absolute;font-size:7.5px;color:var(--ink)}
.amen svg{display:block;margin-bottom:4px}

.room-item{position:absolute;display:flex;align-items:center;gap:12px;font-size:7.5px}
.room-item svg{flex:none}
.rule{left:50px;top:701px;width:412px;height:1px;background:#e2e2e2}

/* sidebar */
.side-blue{left:480px;top:313px;width:150px;height:224px;background:var(--brand)}
.avatar{left:529px;top:296px;width:50px;height:50px;border-radius:50%;background:linear-gradient(160deg,#d8c4ad,#9a7356);border:3px solid var(--white);box-shadow:0 0 0 1px #dcdcdc}
.agent{left:480px;top:357px;width:150px;text-align:center;color:var(--white);line-height:11px}
.agent b{display:block;font-size:10.5px;font-weight:500;line-height:13px}
.agent small{display:block;font-size:7.5px;opacity:.9}
.msg{left:498px;top:396px;width:113px;height:95px;background:var(--white);font-size:7px;color:var(--muted);padding:8px}
.send-msg{left:498px;top:501px;width:113px;height:17px;background:var(--dark);color:var(--white);font-size:7px;display:flex;align-items:center;justify-content:center;gap:5px}
.side-dark{left:480px;top:537px;width:150px;height:164px;background:var(--dark);color:var(--white);text-align:center}
.side-dark .hd{position:absolute;left:0;width:150px;font-size:10.5px;font-weight:500}
.side-dark .ln{position:absolute;left:0;width:150px;font-size:8px}
.side-dark .sep{position:absolute;left:0;top:76px;width:150px;height:1px;background:var(--dark-line)}
.soc{position:absolute;width:16px;height:16px;border:1px solid var(--brand)}
.soc.on{background:var(--brand)}

/* public */
.public-title{left:0;top:721px;width:679px;text-align:center;font-size:10.5px;font-weight:500}
.pub{position:absolute;width:150px;text-align:center;font-size:7.5px}
.pub svg{display:block;margin:0 auto 3px}
.map{left:0;top:810px;width:679px;height:136px;background:linear-gradient(90deg,#e6e6e4,#efefed 50%,#e4e4e2)}

/* footer */
.footer{left:0;top:946px;width:679px;height:254px;background:var(--dark);color:var(--white)}
.f-h{position:absolute;font-size:11px;font-weight:500;color:var(--white)}
.f-phone{left:50px;top:1010px;font-size:13.5px;font-weight:300;color:#d8d8d8}
.f-text{position:absolute;font-size:7px;color:#a9a9a9;line-height:10px}
.f-dir{left:50px;top:1075px;font-size:7px;color:var(--brand);text-decoration:underline}
.f-links{left:226px;top:1012px;font-size:7px;color:#a9a9a9;line-height:16.3px;list-style:none}
.field{position:absolute;background:var(--field);font-size:6.5px;color:#cfcfcf;padding:4px 6px}
.f-send{left:349px;top:1118px;width:53px;height:18px;background:var(--brand);color:var(--white);font-size:7px;display:flex;align-items:center;justify-content:center;gap:4px}
.copy{left:50px;top:1163px;font-size:7px;color:#a9a9a9}
.copy span{color:var(--brand)}
</style>
</head>
<body>

<header class="abs header">
  <div class="abs brand"><span class="brand-mark"></span><span class="brand-name">Lodvenra</span></div>
  <div class="abs brand-tag">Executive Accommodation</div>
  <div class="abs btn-icon"><svg width="8" height="8" viewBox="0 0 24 24"><path d="M6.6 10.8a15 15 0 0 0 6.6 6.6l2.2-2.2c.3-.3.7-.4 1-.2 1.1.4 2.3.6 3.6.6.6 0 1 .4 1 1V20c0 .6-.4 1-1 1A17 17 0 0 1 3 4c0-.6.4-1 1-1h3.5c.6 0 1 .4 1 1 0 1.3.2 2.5.6 3.6.1.3 0 .7-.2 1z" fill="#3276b5"/></svg></div>
  <div class="abs btn-login"><svg width="6" height="6" viewBox="0 0 10 10"><circle cx="5" cy="3" r="2.2" fill="#fff"/><path d="M1 10c0-2.5 1.8-4 4-4s4 1.5 4 4z" fill="#fff"/></svg>Login / Sign Up</div>
  <div class="abs btn-inspect"><svg width="7" height="7" viewBox="0 0 10 10"><rect x="1" y="2" width="8" height="7" fill="none" stroke="#3276b5"/><path d="M1 4h8M3 1v2M7 1v2" stroke="#3276b5"/></svg>Schedule an Inspection</div>
</header>

<div class="abs photo photo-a" role="img" aria-label="Photo of a modern kitchen with bar stools"></div>
<div class="abs photo photo-b" role="img" aria-label="Photo of a shared bedroom with two beds and orange throws"></div>
<div class="abs photo photo-c" role="img" aria-label="Photo of a living room corner with a textured wall"></div>
<div class="abs gal-arrow" style="left:-6px"><svg width="6" height="6" viewBox="0 0 10 10"><path d="M7 1 3 5l4 4" fill="none" stroke="#3276b5" stroke-width="1.5"/></svg></div>
<div class="abs gal-arrow" style="left:667px"><svg width="6" height="6" viewBox="0 0 10 10"><path d="M3 1l4 4-4 4" fill="none" stroke="#3276b5" stroke-width="1.5"/></svg></div>

<div class="abs addr"><svg width="6" height="8" viewBox="0 0 10 14"><path d="M5 0a5 5 0 0 0-5 5c0 4 5 9 5 9s5-5 5-9a5 5 0 0 0-5-5zm0 7a2 2 0 1 1 0-4 2 2 0 0 1 0 4z" fill="#3276b5"/></svg>4410 Harrowgate Ave, KN 60218 - USA</div>
<div class="abs map-link">Show On Map</div>
<h1 class="abs title">1 BK Sharing Rooms for Women at ₹540 in Lorem, Ipsum, USA</h1>
<div class="abs meta">Only for Women &nbsp;|&nbsp; 1 bed available</div>
<div class="abs price">Rental Price: <span>$ 540 - $ 640</span></div>

<section class="abs house">
  <h2 class="abs h2" style="left:50px;top:20px">House Amenities</h2>
  <div class="amen" style="left:50px;top:54px"><svg width="22" height="18" viewBox="0 0 22 18" fill="none" stroke="#555"><rect x="1" y="7" width="20" height="7"/><path d="M3 7V2h16v5M1 14v3M21 14v3M5 7V4h5v3M12 7V4h5v3"/></svg>1 Bedroom</div>
  <div class="amen" style="left:152px;top:54px"><svg width="18" height="18" viewBox="0 0 18 18" fill="none" stroke="#555"><path d="M2 9h14v3a4 4 0 0 1-4 4H6a4 4 0 0 1-4-4zM4 9V3a2 2 0 0 1 4 0"/><circle cx="12" cy="5" r="1"/><circle cx="14" cy="7" r="1"/></svg>1 Bathroom</div>
  <div class="amen" style="left:255px;top:54px"><svg width="20" height="18" viewBox="0 0 20 18" fill="none" stroke="#555"><path d="M4 8V3h12v5M2 8h16v6H2zM3 14v3M17 14v3"/><rect x="6" y="10" width="8" height="3"/></svg>Fully Furnished</div>
  <div class="amen" style="left:358px;top:54px"><svg width="20" height="18" viewBox="0 0 20 18" fill="none" stroke="#555"><path d="M1 8 10 1l9 7v9H1z"/><path d="M5 14h10v-3l-2-2H7l-2 2z"/></svg>Street Parking</div>
</section>

<h2 class="abs h2" style="left:50px;top:534px">Room Amenities</h2>
<div class="room-item" style="left:50px;top:567px"><svg width="15" height="18" viewBox="0 0 15 18" fill="none" stroke="#555"><path d="M2 17V1h11v16M0 17h15"/><circle cx="10" cy="9" r=".8"/></svg>Size of room - xxx sqm</div>
<div class="room-item" style="left:50px;top:598px"><svg width="15" height="16" viewBox="0 0 15 16" fill="none" stroke="#555"><rect x="1" y="1" width="13" height="14"/><path d="M7 1v14M4 6v3"/></svg>Bathroom - Shared</div>
<div class="room-item" style="left:50px;top:629px"><svg width="16" height="16" viewBox="0 0 16 16" fill="none" stroke="#555"><circle cx="8" cy="8" r="7"/><path d="M3 3l10 10M4 8h6"/></svg>Non-Smoking</div>
<div class="room-item" style="left:50px;top:661px"><svg width="16" height="16" viewBox="0 0 16 16" fill="none" stroke="#555"><rect x="1" y="1" width="14" height="14"/><path d="M1 7h14M6 7v8M4 4h2M10 4h2"/></svg>Kitchenette</div>

<div class="room-item" style="left:198px;top:567px"><svg width="18" height="14" viewBox="0 0 18 14" fill="none" stroke="#555"><rect x="1" y="6" width="16" height="5"/><path d="M2 6V1h14v5M1 11v3M17 11v3"/></svg>Bed size - xx - xx ft</div>
<div class="room-item" style="left:198px;top:598px"><svg width="18" height="16" viewBox="0 0 18 16" fill="none" stroke="#555"><circle cx="7" cy="5" r="3.5"/><path d="M1 16c0-4 3-6 6-6s6 2 6 6M12 2a3 3 0 0 1 0 6M14 10c2 1 3 3 3 6"/></svg>Professionals - Housemates</div>
<div class="room-item" style="left:198px;top:629px"><svg width="18" height="16" viewBox="0 0 18 16" fill="none" stroke="#555"><circle cx="9" cy="9" r="1.3"/><path d="M9 10v6M6 6a4 4 0 0 0 0 6M12 6a4 4 0 0 1 0 6M3 3a8 8 0 0 0 0 12M15 3a8 8 0 0 1 0 12"/></svg>High Speed Internet</div>
<div class="room-item" style="left:198px;top:661px"><svg width="14" height="18" viewBox="0 0 14 18" fill="none" stroke="#555"><rect x="1" y="1" width="12" height="16"/><path d="M7 1v16M5 8v2M9 8v2"/></svg>Wardrobe</div>

<div class="room-item" style="left:347px;top:567px"><svg width="18" height="15" viewBox="0 0 18 15" fill="none" stroke="#555"><rect x="1" y="1" width="16" height="10"/><path d="M6 14h6M9 11v3"/></svg>TV</div>
<div class="room-item" style="left:347px;top:598px"><svg width="18" height="16" viewBox="0 0 18 16" fill="none" stroke="#555"><path d="M1 7h16M2 7v9M16 7v9M5 1h8v6H5z"/><path d="M12 10h3v6"/></svg>Workstation</div>
<div class="room-item" style="left:347px;top:629px"><svg width="18" height="16" viewBox="0 0 18 16" fill="none" stroke="#555"><path d="M1 8h16v3a4 4 0 0 1-4 4H5a4 4 0 0 1-4-4zM11 2a3 3 0 0 1 5 0M13 4v1M15 4v1"/></svg>Ensuite Shower</div>
<div class="room-item" style="left:347px;top:661px"><svg width="18" height="16" viewBox="0 0 18 16" fill="none" stroke="#555"><rect x="1" y="1" width="16" height="14"/><path d="M1 6h16M1 11h16M7 3h4M7 8h4M7 13h4"/></svg>Storage Space</div>
<div class="abs rule"></div>

<aside>
  <div class="abs side-blue"></div>
  <div class="abs avatar" role="img" aria-label="Host portrait"></div>
  <div class="abs agent"><b>Maren Ellery</b><small>Contrary popular</small></div>
  <div class="abs msg">Write A Message ...</div>
  <div class="abs send-msg"><svg width="7" height="6" viewBox="0 0 10 8"><path d="M0 0l10 4-10 4 2-4z" fill="#fff"/></svg>Send Message</div>
  <div class="abs side-dark">
    <div class="hd" style="top:17px">Contact Info</div>
    <div class="ln" style="top:38px">Call Us: 555 - 204 - 3187</div>
    <div class="ln" style="top:49px;text-decoration:underline">hello@lodvenra.com</div>
    <div class="sep"></div>
    <div class="hd" style="top:92px">Share to a Friend</div>
    <span class="soc" style="left:18px;top:116px"></span>
    <span class="soc on" style="left:42px;top:116px"></span>
    <span class="soc" style="left:66px;top:116px"></span>
    <span class="soc" style="left:90px;top:116px"></span>
    <span class="soc" style="left:114px;top:116px"></span>
  </div>
</aside>

<h2 class="abs public-title">Public Amenities..</h2>
<div class="pub" style="left:41px;top:752px"><svg width="16" height="18" viewBox="0 0 16 18" fill="none" stroke="#555"><rect x="2" y="1" width="12" height="12" rx="2"/><path d="M2 7h12M5 10h.1M11 10h.1M4 13l-2 4M12 13l2 4"/></svg>Trains Station</div>
<div class="pub" style="left:190px;top:752px"><svg width="18" height="18" viewBox="0 0 18 18" fill="none" stroke="#555"><rect x="5" y="1" width="12" height="14" rx="1"/><path d="M5 8h12M8 12h.1M14 12h.1M2 4v12M1 4h3"/></svg>Busses Station</div>
<div class="pub" style="left:339px;top:752px"><svg width="16" height="18" viewBox="0 0 16 18" fill="none" stroke="#555"><path d="M1 17h14M3 17V6h5v11M8 17V1h6v16M5 9h1M5 12h1M10 4h2M10 7h2M10 10h2"/></svg>Distance to the City</div>
<div class="pub" style="left:489px;top:752px"><svg width="16" height="18" viewBox="0 0 16 18" fill="none" stroke="#555"><path d="M8 1a6 6 0 0 0-6 6c0 4 6 9 6 9s6-5 6-9a6 6 0 0 0-6-6z"/><circle cx="8" cy="7" r="2"/><path d="M2 17h12"/></svg>MAP of the Area</div>

<div class="abs map" role="img" aria-label="Map of the central United States around the listing"></div>

<footer class="abs footer"></footer>
<h3 class="f-h" style="left:50px;top:988px">Contact Us</h3>
<div class="abs f-phone">555 - 204 - 3187</div>
<div class="f-text" style="left:50px;top:1027px;font-size:7.5px">hello@lodvenra.com</div>
<div class="f-text" style="left:50px;top:1046px">4410 Harrowgate Ave<br>Corvale, KN 60218</div>
<div class="abs f-dir">Get A Directions</div>
<span class="soc" style="left:50px;top:1118px;width:18px;height:18px"></span>
<span class="soc on" style="left:72px;top:1118px;width:18px;height:18px"></span>
<span class="soc" style="left:94px;top:1118px;width:18px;height:18px"></span>
<span class="soc" style="left:117px;top:1118px;width:18px;height:18px"></span>

<h3 class="f-h" style="left:226px;top:988px">Quick Links</h3>
<ul class="abs f-links"><li>Home</li><li>About Us</li><li>Services</li><li>Portfolio</li><li>Testimonials</li><li>News</li><li>Contact Us</li></ul>

<h3 class="f-h" style="left:349px;top:988px">How Can We Help?</h3>
<div class="field" style="left:349px;top:1014px;width:135px;height:18px">Name</div>
<div class="field" style="left:494px;top:1014px;width:135px;height:18px">Phone</div>
<div class="field" style="left:349px;top:1042px;width:280px;height:17px">Email</div>
<div class="field" style="left:349px;top:1069px;width:280px;height:40px">Message</div>
<div class="abs f-send"><svg width="7" height="6" viewBox="0 0 10 8"><path d="M0 0l10 4-10 4 2-4z" fill="#fff"/></svg>Send</div>
<div class="abs copy">© 2019 <span>Lodvenra</span>. All rights reserved.</div>
<svg class="abs" style="left:618px;top:1161px" width="11" height="13" viewBox="0 0 11 13"><path d="M5.5 0 11 13 5.5 9.5 0 13z" fill="#3276b5"/></svg>

</body>
</html>
```